Pathways to Brightmoor Land Ventures

size of the ad - 8”x 10.75" plus 0.25" bleed
I would like an ad for a magazine that will stand out and make people want to read the ad.
The ad should not be crowded and people reading the ad will be able to read the text.
I would like it to be a creative and modern-day design.
the list of topics should not be the focus of the ad.
the text is attached.
If you decide to use people in the ad then please no ladies.
please note that leave over 1 inch for the bottom of the footer

```html
<!DOCTYPE html>
<html lang="en">
<head>
<meta charset="utf-8">
<title>Real Estate Course</title>
<link href="https://fonts.googleapis.com/css2?family=Montserrat:ital,wght@0,400;0,600;0,800;1,400&family=Oswald:wght@300;700&family=Caveat:wght@500&display=swap" rel="stylesheet">
<style>
  :root {
    --navy-deep: #1a2357;
    --navy-mid: #233a9c;
    --blue-bright: #2d56e0;
    --white: #ffffff;
    --soft-white: #e8ecfb;
    --stone-light: #b9b6b3;
    --stone-dark: #3a3c44;
  }
  html, body {
    margin: 0;
    padding: 0;
    width: 893px;
    height: 1200px;
    overflow: hidden;
    background: #ffffff;
  }
  .ad {
    position: relative;
    width: 893px;
    height: 1200px;
    overflow: hidden;
    background: linear-gradient(180deg, var(--navy-deep) 0%, var(--navy-mid) 45%, var(--blue-bright) 80%);
    color: var(--white);
    font-family: "Montserrat", sans-serif;
  }
  .headline {
    position: absolute;
    left: 58px;
    top: 70px;
    margin: 0;
    font-weight: 800;
    font-size: 92px;
    line-height: 0.98;
    letter-spacing: 1px;
  }
  .headline .light { font-weight: 400; }
  .program-name {
    position: absolute;
    left: 60px;
    top: 272px;
    margin: 0;
    font-weight: 600;
    font-size: 22px;
  }
  .session-info {
    position: absolute;
    left: 612px;
    top: 182px;
    font-size: 15px;
    line-height: 1.35;
  }
  .session-info .town {
    font-weight: 800;
    font-size: 30px;
    margin-bottom: 4px;
  }
  .tagline {
    position: absolute;
    left: 60px;
    right: 60px;
    top: 350px;
    margin: 0;
    text-align: center;
    font-family: "Caveat", cursive;
    font-size: 38px;
    font-weight: 500;
    padding-bottom: 8px;
    border-bottom: 2px solid var(--white);
  }
  .topics {
    position: absolute;
    left: 64px;
    top: 462px;
  }
  .topics h2 {
    margin: 0 0 10px;
    font-size: 20px;
    font-weight: 600;
  }
  .topics ul {
    margin: 0;
    padding-left: 22px;
    font-style: italic;
    font-size: 19px;
    line-height: 34px;
  }
  .offer {
    position: absolute;
    left: 650px;
    top: 520px;
    width: 220px;
  }
  .offer h2 {
    margin: 0;
    font-weight: 800;
    font-size: 44px;
    line-height: 1.05;
  }
  .offer p {
    margin: 14px 0 0;
    font-family: "Oswald", sans-serif;
    font-weight: 300;
    font-size: 27px;
    line-height: 1.2;
    text-transform: uppercase;
  }
  .building {
    position: absolute;
    left: 0;
    bottom: 0;
    width: 893px;
    height: 420px;
  }
</style>
</head>
<body>
  <main class="ad">
    <h1 class="headline">REAL <span class="light">ESTATE</span><br>COURSE</h1>
    <p class="program-name">Pathways to Brightmoor Land Ventures</p>

    <div class="session-info">
      <div class="town">Brightmoor</div>
      <div>10 Tuesday evenings sessions</div>
      <div>Starting Feb.28</div>
      <div>Limited Partial Scholarships</div>
    </div>

    <p class="tagline">Investing in knowledge is investing in opportunities</p>

    <section class="topics">
      <h2>Topics : partial listing</h2>
      <ul>
        <li>Real estate investment strategies</li>
        <li>Due diligence</li>
        <li>Financing</li>
        <li>Underwriting</li>
        <li>Property management</li>
        <li>Real estate Legal basics</li>
        <li>Sourcing deals</li>
        <li>Syndication</li>
        <li>Dealing with brokers</li>
        <li>Tax fundamentals</li>
      </ul>
    </section>

    <section class="offer">
      <h2>EARLY<br>BIRD<br>SPECIAL</h2>
      <p>For those that started or would like to go into real estate</p>
    </section>

    <svg class="building" viewBox="0 0 893 420" role="img" aria-label="Photo of a modern multi-storey brick office building seen from below">
      <defs>
        <linearGradient id="stone" x1="0" y1="0" x2="1" y2="1">
          <stop offset="0" stop-color="#c9c6c2"/>
          <stop offset="0.5" stop-color="#8d8b8c"/>
          <stop offset="1" stop-color="#3a3c44"/>
        </linearGradient>
      </defs>
      <polygon points="40,420 40,170 280,40 430,28 893,70 893,420" fill="url(#stone)"/>
    </svg>
  </main>
</body>
</html>
```